Graphic Banner Design - 2.5' x 6' - High Tech Company

We are in need of a banner design for an outdoor sign that will be used at sponsorship events.

Size
2.5' x 6'

The company is a high tech company, and the design will be used for action sports events. So lining up to that would be good.

Tag line to be incorporated...
"Extreme IT Services for Extreme Needs."

Target Market(s)

Business Owners, Entrepreneurs, IT Professionals.

Industry/Entity Type

Information Technology

Logo Text

Vexlora

Colors

Designer to choose colors to be used in the design.

Requirements
Must have
• Must feel young and vibrant, fit in to an action sports event and just be out of this world awesome.
• In the world of the IT, we are the Zanverolli. Fast, Awesome, not necessarily cheap, but you know it will do what you want extremely well. Not for everyone, but always desired.

```html
<!DOCTYPE html>
<html lang="en">
<head>
<meta charset="utf-8">
<title>Vexlora – Event Banner</title>
<link rel="stylesheet" href="https://fonts.googleapis.com/css2?family=Montserrat:wght@500&family=Open+Sans:ital,wght@0,600;0,700;1,300&display=swap">
<style>
  :root {
    --page-bg: #e9eaeb;
    --teal-light: #22a7c0;
    --teal-dark: #0b7696;
    --teal-glow: #42cfd2;
    --orange: #f0780f;
    --ink: #1c2430;
    --ink-soft: #3a4e5c;
    --white: #ffffff;
    --crowd-a: #6a6f9a;
    --crowd-b: #9aa3c8;
    --crowd-c: #3e3f60;
  }
  html, body {
    margin: 0;
    width: 1200px;
    height: 800px;
    overflow: hidden;
    background: var(--page-bg);
  }
  .banner {
    position: absolute;
    left: 20px;
    top: 158px;
    width: 1160px;
    height: 484px;
    display: block;
  }
  .brand-name {
    font-family: "Montserrat", sans-serif;
    font-weight: 500;
    font-size: 28px;
    fill: var(--ink);
  }
  .brand-mark { fill: var(--ink); }
  .event-line {
    font-family: "Open Sans", sans-serif;
    font-weight: 600;
    font-size: 31px;
    fill: var(--white);
  }
  .tagline-lead {
    font-family: "Open Sans", sans-serif;
    font-style: italic;
    font-weight: 300;
    font-size: 40px;
    fill: var(--ink-soft);
  }
  .tagline-main {
    font-family: "Open Sans", sans-serif;
    font-weight: 700;
    font-size: 45px;
    fill: var(--white);
  }
  .web-address {
    font-family: "Open Sans", sans-serif;
    font-weight: 600;
    font-size: 20px;
    fill: var(--ink);
  }
  .icon-line { fill: none; stroke: var(--orange); stroke-width: 2.5; }
  .icon-fill { fill: var(--orange); }
</style>
</head>
<body>
<svg class="banner" viewBox="0 0 1474 615" xmlns="http://www.w3.org/2000/svg">
  <defs>
    <linearGradient id="bg-teal" x1="0" y1="0" x2="1" y2="1">
      <stop offset="0" stop-color="var(--teal-light)"/>
      <stop offset="1" stop-color="var(--teal-dark)"/>
    </linearGradient>
    <linearGradient id="crowd-tone" x1="0" y1="0" x2="1" y2="1">
      <stop offset="0" stop-color="var(--crowd-c)"/>
      <stop offset="0.5" stop-color="var(--crowd-b)"/>
      <stop offset="1" stop-color="var(--crowd-a)"/>
    </linearGradient>
    <radialGradient id="hud-glow" cx="0.5" cy="0.5" r="0.5">
      <stop offset="0" stop-color="#6fe0ee" stop-opacity="0.45"/>
      <stop offset="1" stop-color="#6fe0ee" stop-opacity="0"/>
    </radialGradient>
    <radialGradient id="top-glow" cx="0.5" cy="0.5" r="0.5">
      <stop offset="0" stop-color="#5fe3f0" stop-opacity="0.4"/>
      <stop offset="1" stop-color="#5fe3f0" stop-opacity="0"/>
    </radialGradient>
  </defs>

  <rect class="banner-bg" width="1474" height="615" fill="url(#bg-teal)"/>

  <circle class="tech-decoration" cx="1280" cy="190" r="190" fill="url(#hud-glow)"
          role="img" aria-label="Faint glowing technology interface rings"/>
  <ellipse class="brand-glow" cx="737" cy="60" rx="160" ry="80" fill="url(#top-glow)"/>

  <polygon class="accent-band-top" points="0,115 445,115 545,210 525,210 430,133 0,133"
           fill="var(--teal-glow)" opacity="0.75"/>

  <polygon class="event-photo"
           points="0,133 380,133 530,210 925,210 1010,300 1474,300 1474,318 1140,318 935,540 620,540 530,615 0,615"
           fill="url(#crowd-tone)" role="img"
           aria-label="Photo of a cheering crowd in front of a concert stage"/>

  <polygon class="accent-orange" points="925,208 972,208 1045,300 1010,300" fill="var(--orange)"/>

  <g class="brand">
    <circle class="brand-mark" cx="737" cy="88" r="30"/>
    <line x1="525" y1="155" x2="675" y2="155" stroke="var(--ink)" stroke-width="2"/>
    <text class="brand-name" x="737" y="165" text-anchor="middle">Vexlora</text>
    <line x1="799" y1="155" x2="949" y2="155" stroke="var(--ink)" stroke-width="2"/>
  </g>

  <text class="event-line" x="1048" y="258" textLength="345" lengthAdjust="spacingAndGlyphs">An action sports event</text>

  <text class="tagline-lead" x="1051" y="470" textLength="395" lengthAdjust="spacingAndGlyphs">Extreme IT Services for</text>
  <text class="tagline-main" x="1082" y="527" textLength="336" lengthAdjust="spacingAndGlyphs">Extreme Needs</text>

  <polygon class="footer-stripe" points="625,577 1474,577 1474,615 1025,615 1000,591 640,591" fill="var(--orange)"/>
  <text class="web-address" x="1106" y="606" textLength="293" lengthAdjust="spacing">WWW.VEXLORA.COM</text>

  <g class="contact-icons">
    <circle class="icon-line" cx="29" cy="527" r="17"/>
    <path class="icon-fill" d="M21 520 q2-4 5-2 l2 4 q1 2-1 3 q2 5 7 7 q1-2 3-1 l4 2 q2 3-2 5 q-10 0-18-18z"/>
    <path class="icon-fill" d="M29 558 a13 13 0 0 1 13 13 c0 9-13 24-13 24 s-13-15-13-24 a13 13 0 0 1 13-13z"/>
    <circle cx="29" cy="571" r="5" fill="var(--crowd-c)"/>
  </g>
</svg>
</body>
</html>
```